Bref créative
Law firm stationary package
Letterhead, business card, envelope
Professional
Theodore R. Wexley
Attorney at Law
5183 Poldin Lane, Suite A
P.O. Box 81947
Ashbury, IN 45867
Ted@WexleyCounsel.example
www.WexleyCounsel.example
Please create business card, letterhead, and envelope designs.
Focus on clean, professional design for this corporate law firm. Stay away from watermarks, waves, or anything that is too ink-intensive. You may use either or both of the attached logos.
Main logo
Inverse of logo, use is optional

```html
<!DOCTYPE html>
<html lang="en">
<head>
<meta charset="utf-8">
<title>Wexley Counsel – Business Card</title>
<link rel="stylesheet" href="https://fonts.googleapis.com/css2?family=Cinzel:wght@400;600&family=Cormorant+Garamond:wght@500;600&display=swap">
<style>
  :root {
    --navy: #2e2d7f;
    --grey: #8a8b90;
    --grey-band: #7d7e83;
    --text-grey: #6b6c72;
    --paper: #ffffff;
    --backdrop: #e9e6e1;
  }
  * { margin: 0; padding: 0; box-sizing: border-box; }
  html, body { width: 1200px; height: 914px; overflow: hidden; background: var(--backdrop); }
  .canvas { position: relative; width: 1200px; height: 914px; }
  .card {
    position: absolute; left: 100px; top: 171px;
    width: 1000px; height: 572px;
    background: var(--paper);
    box-shadow: 0 10px 30px rgba(0,0,0,0.12);
    overflow: hidden;
  }
  .brand-mark {
    position: absolute; left: 236px; top: 132px;
    width: 76px; height: 76px; background: var(--navy);
  }
  .brand-divider {
    position: absolute; left: 392px; top: 120px;
    width: 1px; height: 110px; background: var(--grey);
  }
  .brand-name {
    position: absolute; left: 420px; top: 122px;
    font-family: 'Cinzel', serif; font-weight: 400; color: var(--navy);
    line-height: 1;
  }
  .brand-name .primary { display: block; font-size: 64px; letter-spacing: 1px; }
  .brand-name .secondary { display: block; font-size: 26px; letter-spacing: 2px; margin-top: 10px; padding-left: 60px; }
  .person {
    position: absolute; right: 612px; top: 282px; text-align: right;
    font-family: 'Cormorant Garamond', serif; font-variant: small-caps;
  }
  .person .name { color: var(--navy); font-size: 26px; font-weight: 600; letter-spacing: 1px; }
  .person .title { color: var(--text-grey); font-size: 21px; font-weight: 500; margin-top: 2px; }
  .person .address { color: var(--text-grey); font-size: 20px; font-weight: 500; margin-top: 14px; line-height: 1.3; }
  .contact-list {
    position: absolute; left: 452px; top: 280px; list-style: none;
    font-family: 'Cormorant Garamond', serif; font-variant: small-caps;
    color: var(--text-grey); font-size: 20px; font-weight: 500;
  }
  .contact-list li { display: flex; align-items: center; height: 27px; }
  .contact-list svg { width: 16px; height: 16px; margin-right: 10px; flex: none; }
  .bottom-bands { position: absolute; left: 0; bottom: 0; width: 1000px; height: 90px; }
</style>
</head>
<body>
<div class="canvas">
  <div class="card">
    <div class="brand-mark" aria-hidden="true"></div>
    <div class="brand-divider"></div>
    <div class="brand-name">
      <span class="primary">Wexley</span>
      <span class="secondary">Counsel, LLC</span>
    </div>

    <div class="person">
      <div class="name">Theodore R. Wexley</div>
      <div class="title">Attorney at Law</div>
      <div class="address">5183 Poldin Lane, Suite A<br>81947 Ashbury, IN 45867</div>
    </div>

    <ul class="contact-list">
      <li><svg viewBox="0 0 16 16"><circle cx="8" cy="8" r="8" fill="var(--grey)"/><path d="M5 4.5l1.6-.5 1 2-1 .8a5 5 0 0 0 2.6 2.6l.8-1 2 1-.5 1.6c-3.5 0-6.5-3-6.5-6.5z" fill="#fff"/></svg>555.204.7381</li>
      <li><svg viewBox="0 0 16 16"><circle cx="8" cy="8" r="8" fill="var(--grey)"/><path d="M5 4.5l1.6-.5 1 2-1 .8a5 5 0 0 0 2.6 2.6l.8-1 2 1-.5 1.6c-3.5 0-6.5-3-6.5-6.5z" fill="#fff"/></svg>555.618.2094</li>
      <li><svg viewBox="0 0 16 16"><circle cx="8" cy="8" r="8" fill="var(--grey)"/><rect x="4.5" y="6.5" width="7" height="4" fill="#fff"/><rect x="5.5" y="4" width="5" height="2.5" fill="#fff"/></svg>555.372.4406</li>
      <li><svg viewBox="0 0 16 16"><circle cx="8" cy="8" r="8" fill="var(--grey)"/><rect x="4" y="5.5" width="8" height="5" fill="#fff"/><path d="M4 5.5l4 3 4-3" stroke="var(--grey)" fill="none" stroke-width="0.8"/></svg>Ted@WexleyCounsel.example</li>
      <li><svg viewBox="0 0 16 16"><circle cx="8" cy="8" r="8" fill="var(--grey)"/><circle cx="8" cy="8" r="4" fill="none" stroke="#fff" stroke-width="1"/><path d="M4 8h8M8 4v8" stroke="#fff" stroke-width="0.8"/></svg>www.WexleyCounsel.example</li>
    </ul>

    <svg class="bottom-bands" viewBox="0 0 1000 90" preserveAspectRatio="none" aria-hidden="true">
      <polygon points="0,22 470,22 520,90 0,90" fill="var(--navy)"/>
      <polygon points="470,22 1000,22 1000,90 520,90" fill="var(--grey-band)"/>
    </svg>
  </div>
</div>
</body>
</html>
```